Your online mall needs the design of a banner ad

I need the design of a banner to publicize the website in local internet media. It has to attract the visitor from the middle, so it should be flashy but attractive. The website is an ecommerce. It is an online shopping center with more than 12,000 products and 18 different categories. The website is: www.vendolira.com Allowed file formats: JPG, PNG or GIF (never more than 30 seconds) File size: maximum 150KB Banner size: large rectangle 300x600 The banner should contain the following: -Logo de la brand (attached file) -Web site: www.vendolira.com - Phrase: "Your online shopping center" -Frame: "of 12,000 products of the leading brands of the market at the price of vendolira" -Frame: "Up to -70% Dto . " -Print key that can attract: REMATE (optional), UNCOVER (optional)

```html
<!DOCTYPE html>
<html lang="es">
<head>
<meta charset="utf-8">
<title>Vendolira – banners 300x600</title>
<link rel="stylesheet" href="https://fonts.googleapis.com/css2?family=Montserrat:wght@500;600;700&family=Open+Sans:wght@400;600&display=swap">
<style>
  :root {
    --sheet: #d3d3d3;
    --navy: #2d3446;
    --orange: #f7941d;
    --white: #ffffff;
    --label: #2b2b2b;
    --photo-top: #a9aaa8;
    --photo-mid: #8f918f;
    --photo-low: #8a5a3a;
  }
  * { margin: 0; padding: 0; box-sizing: border-box; }
  html, body { width: 1200px; height: 1200px; overflow: hidden; background: var(--sheet); }
  body { position: relative; font-family: "Montserrat", sans-serif; }

  .frame-label {
    position: absolute; top: 333px; width: 240px; text-align: center;
    font-size: 18px; font-weight: 600; color: var(--label); letter-spacing: 0.2px;
  }

  .banner {
    position: absolute; top: 383px; width: 240px; height: 480px; overflow: hidden;
    background: var(--white); box-shadow: 0 2px 4px rgba(0,0,0,0.35);
  }
  .banner-art { position: absolute; inset: 0; width: 240px; height: 480px; }

  .brand { position: absolute; left: 12px; top: 20px; display: flex; align-items: center; gap: 9px; }
  .brand-dot { width: 30px; height: 30px; border-radius: 50%; background: var(--orange); }
  .brand-name { font-size: 29px; font-weight: 700; color: var(--navy); line-height: 1; letter-spacing: -0.3px; }

  .bracket {
    position: absolute; left: 30px; width: 66px;
    border-top: 1.5px solid var(--orange); border-bottom: 1.5px solid var(--orange); border-left: 1.5px solid var(--orange);
  }

  .headline { position: absolute; left: 0; width: 240px; text-align: center; color: var(--white); font-weight: 600; }
  .accent { color: var(--orange); }

  .tagline { top: 334px; font-size: 24px; line-height: 28px; letter-spacing: -0.3px; }
  .catalog { top: 326px; font-size: 13.4px; line-height: 22.6px; letter-spacing: -0.4px; left: 8px; }

  .offer-lead { position: absolute; left: 42px; top: 336px; font-size: 19px; font-weight: 600; color: var(--white); }
  .offer-value { position: absolute; left: 40px; top: 346px; font-size: 68px; font-weight: 700; color: var(--orange); letter-spacing: -2px; line-height: 80px; }
  .offer-tail { position: absolute; left: 132px; top: 412px; font-size: 17px; font-weight: 600; color: var(--white); }

  .site {
    position: absolute; left: 0; width: 240px; top: 446px; display: flex; justify-content: center; align-items: center; gap: 4px;
    font-family: "Open Sans", sans-serif; font-size: 17.5px; color: var(--orange);
  }
  .site-icon { width: 15px; height: 15px; }
</style>
</head>
<body>

<div class="frame-label" style="left:164px">FRAME-1</div>
<div class="frame-label" style="left:476px">FRAME-2</div>
<div class="frame-label" style="left:797px">FRAME-3</div>

<!-- Frame 1 -->
<section class="banner" style="left:164px">
  <svg class="banner-art" viewBox="0 0 300 600" preserveAspectRatio="none">
    <defs>
      <linearGradient id="photo-1" x1="0" y1="0" x2="0" y2="1">
        <stop offset="0" stop-color="#b4b5b3"/><stop offset="0.55" stop-color="#949693"/><stop offset="0.8" stop-color="#8a5a3a"/><stop offset="1" stop-color="#6e4128"/>
      </linearGradient>
    </defs>
    <circle cx="160" cy="300" r="225" fill="url(#photo-1)" role="img" aria-label="Foto: carrito de compras con bolsas de colores y un portátil sobre una mesa"/>
    <path d="M0,290 C40,270 85,272 125,300 C170,335 210,370 250,370 C275,370 290,362 300,350 L300,600 L0,600 Z" fill="#2d3446"/>
  </svg>
  <div class="brand"><span class="brand-dot"></span><span class="brand-name">Vendolira</span></div>
  <div class="bracket" style="top:327px;height:100px"></div>
  <div class="headline tagline">TU CENTRO<br>COMERCIAL<br><span class="accent">ONLINE</span></div>
  <div class="site">
    <svg class="site-icon" viewBox="0 0 16 16"><circle cx="8" cy="8" r="7.5" fill="#f7941d"/><g fill="none" stroke="#fff" stroke-width="0.9"><circle cx="8" cy="8" r="4.6"/><ellipse cx="8" cy="8" rx="2" ry="4.6"/><line x1="3.4" y1="8" x2="12.6" y2="8"/></g></svg>
    <span>www.vendolira.com</span>
  </div>
</section>

<!-- Frame 2 -->
<section class="banner" style="left:476px">
  <svg class="banner-art" viewBox="0 0 300 600" preserveAspectRatio="none">
    <defs>
      <linearGradient id="photo-2" x1="0" y1="0" x2="0" y2="1">
        <stop offset="0" stop-color="#b4b5b3"/><stop offset="0.55" stop-color="#949693"/><stop offset="0.8" stop-color="#8a5a3a"/><stop offset="1" stop-color="#6e4128"/>
      </linearGradient>
    </defs>
    <circle cx="160" cy="300" r="225" fill="url(#photo-2)" role="img" aria-label="Foto: carrito de compras con bolsas de colores y un portátil sobre una mesa"/>
    <path d="M0,290 C40,270 85,272 125,300 C170,335 210,370 250,370 C275,370 290,362 300,350 L300,600 L0,600 Z" fill="#2d3446"/>
  </svg>
  <div class="brand"><span class="brand-dot"></span><span class="brand-name">Vendolira</span></div>
  <div class="bracket" style="top:320px;height:121px"></div>
  <div class="headline catalog">DE <span class="accent">12.000</span> PRODUCTOS<br>DE LAS MARCAS<br>LIDERES DEL<br>MERCADO A PRECIO DE<br><span class="accent">VENDOLIRA</span></div>
  <div class="site">
    <svg class="site-icon" viewBox="0 0 16 16"><circle cx="8" cy="8" r="7.5" fill="#f7941d"/><g fill="none" stroke="#fff" stroke-width="0.9"><circle cx="8" cy="8" r="4.6"/><ellipse cx="8" cy="8" rx="2" ry="4.6"/><line x1="3.4" y1="8" x2="12.6" y2="8"/></g></svg>
    <span>www.vendolira.com</span>
  </div>
</section>

<!-- Frame 3 -->
<section class="banner" style="left:797px">
  <svg class="banner-art" viewBox="0 0 300 600" preserveAspectRatio="none">
    <defs>
      <linearGradient id="photo-3" x1="0" y1="0" x2="0" y2="1">
        <stop offset="0" stop-color="#b4b5b3"/><stop offset="0.55" stop-color="#949693"/><stop offset="0.8" stop-color="#8a5a3a"/><stop offset="1" stop-color="#6e4128"/>
      </linearGradient>
    </defs>
    <circle cx="160" cy="300" r="225" fill="url(#photo-3)" role="img" aria-label="Foto: carrito de compras con bolsas de colores y un portátil sobre una mesa"/>
    <path d="M0,290 C40,270 85,272 125,300 C170,335 210,370 250,370 C275,370 290,362 300,350 L300,600 L0,600 Z" fill="#2d3446"/>
  </svg>
  <div class="brand"><span class="brand-dot"></span><span class="brand-name">Vendolira</span></div>
  <div class="bracket" style="top:328px;height:104px"></div>
  <div class="offer-lead">HASTA</div>
  <div class="offer-value">70%</div>
  <div class="offer-tail">DTO</div>
  <div class="site">
    <svg class="site-icon" viewBox="0 0 16 16"><circle cx="8" cy="8" r="7.5" fill="#f7941d"/><g fill="none" stroke="#fff" stroke-width="0.9"><circle cx="8" cy="8" r="4.6"/><ellipse cx="8" cy="8" rx="2" ry="4.6"/><line x1="3.4" y1="8" x2="12.6" y2="8"/></g></svg>
    <span>www.vendolira.com</span>
  </div>
</section>

</body>
</html>
```